Flyer for American Indian Elders on Dementia Warning Signs

We need a flyer designed for older adults who are American Indian or Alaska Native (in the U.S.).

Ideally, the flyer should complement the colors of our logos. The project logo and our organization logo are attached to the brief.

When people see the flyer we want them to feel that it represents their culture, is warm, and professional but relatable to older adults and people who have limited incomes.

I have attached an earlier draft of the document we designed ourselves BUT we want different and better.

It is for older adults who have trouble reading so:
1. you must use a font that is 11.5 points or larger
2. Do not put text over complex pictures or use shading with words
3. You can use a serif font for the heading, but should use san serif for the body text
4. There should be good contrast between the font color and background

Please do not use any images that include a head dress or pictures of American Indian people or things that are very traditional or "token" imagery.

We need to save a small space under the call out box/ somewhere on the flyer for other people to add their logo once they download.

Let us know if you have questions or need additional information.

Target Market(s)

Older American Indian people

Font styles to use
Serif
Sans Serif

Requirements
Must have
• Easy to read for older adults
Should not have
• indian headdress

```html
<!DOCTYPE html>
<html lang="en">
<head>
<meta charset="utf-8">
<title>10 Signs of Thinking or Memory Changes – Flyer</title>
<link rel="stylesheet" href="https://fonts.googleapis.com/css2?family=Open+Sans:wght@300;400;600;700;800&display=swap">
<style>
  :root{
    --clay:#b65b54;
    --teal:#4aa6ab;
    --teal-dark:#3a979d;
    --ink:#555b5e;
    --white:#ffffff;
    --backdrop:#e4e1df;
    --photo-a:#c9a48e;
    --photo-b:#8f7568;
  }
  *{box-sizing:border-box;margin:0;padding:0}
  html,body{width:1200px;height:418px;overflow:hidden}
  body{background:var(--backdrop);font-family:"Open Sans",Arial,sans-serif;position:relative}
  .page{position:absolute;top:0;width:296px;height:418px;overflow:hidden;background:var(--white)}
  .page--front{left:270px}
  .page--back{left:634px;background:var(--teal)}
  .page-art{position:absolute;inset:0}

  /* front */
  .facts{position:absolute;left:0;top:172px;width:140px;padding:0 6px 0 10px;color:var(--white);font-weight:700;font-size:8.2px;line-height:1.13;list-style:none}
  .facts li{position:relative;padding-left:6px;margin-bottom:8px}
  .facts li::before{content:"";position:absolute;left:0;top:3px;width:4px;height:4px;border-radius:50%;background:var(--white)}

  .title{position:absolute;left:136px;top:114px;width:154px;text-align:right;font-weight:700;white-space:nowrap}
  .title-line{display:block}
  .title-line--top{line-height:38px;height:38px}
  .t-ten{font-size:42px;font-weight:800;color:var(--clay);letter-spacing:-2px}
  .t-signs{font-size:16px;font-weight:700;color:var(--clay)}
  .t-light{font-weight:300}
  .t-teal{font-size:18px;line-height:17px;color:var(--teal-dark);font-weight:700}
  .t-might{font-size:16px;line-height:18px;color:var(--teal-dark);font-weight:300}
  .t-dementia{font-size:24px;line-height:24px;color:var(--clay);font-weight:800;letter-spacing:-.3px}

  .intro{position:absolute;left:142px;top:253px;width:150px;text-align:center;font-size:6.8px;line-height:1.27;color:var(--ink)}
  .learn{position:absolute;left:0;top:346px;width:296px;height:29px;background:var(--teal);color:var(--white);font-weight:700;font-size:7.1px;line-height:1.2;text-align:center;padding-top:3px}
  .partners{position:absolute;left:0;top:375px;width:296px;height:33px;display:flex;align-items:center;justify-content:space-around;padding:0 10px}
  .partner{display:flex;align-items:center;gap:5px;font-weight:700;font-size:7.4px;line-height:1.1}
  .partner i{display:block;width:14px;height:14px;border-radius:50%}
  .partner--one{color:var(--clay)}
  .partner--one i{background:var(--teal)}
  .partner--two{color:var(--teal-dark)}
  .partner--two i{background:var(--clay)}
  .strip{position:absolute;left:0;bottom:0;width:296px;height:10px;background:var(--teal)}

  /* back */
  .ask{position:absolute;left:14px;top:142px;color:var(--white);font-weight:800;font-size:25px;line-height:.98;letter-spacing:-.3px}
  .ask p+p{margin-top:8px}
  .signs{position:absolute;left:160px;top:10px;width:132px;color:var(--white);font-size:5.5px;line-height:1.18;list-style:none;counter-reset:sign}
  .signs>li{counter-increment:sign;position:relative;padding-left:10px;margin-bottom:4.2px;font-weight:700}
  .signs>li::before{content:counter(sign) ".";position:absolute;left:0;top:0}
  .signs ul{list-style:none;font-weight:400;margin-top:1px}
  .signs ul li{position:relative;padding-left:5px}
  .signs ul li::before{content:"•";position:absolute;left:0}
</style>
</head>
<body>

<article class="page page--front">
  <svg class="page-art" viewBox="0 0 296 418" width="296" height="418">
    <defs>
      <linearGradient id="elders-photo" x1="0" y1="0" x2="1" y2="1">
        <stop offset="0" stop-color="#d8cbbd"/>
        <stop offset=".5" stop-color="var(--photo-a)"/>
        <stop offset="1" stop-color="var(--photo-b)"/>
      </linearGradient>
    </defs>
    <rect x="0" y="110" width="140" height="236" fill="var(--clay)"/>
    <path d="M0 0H296V118C258 114 220 128 190 148C165 165 130 170 100 158C65 144 30 118 0 116Z" fill="url(#elders-photo)" role="img" aria-label="Photo of smiling older adults cheering together on a sofa"/>
  </svg>

  <ul class="facts">
    <li>American Indian and Alaska Native people have a high risk of dementia.</li>
    <li>Big changes in memory or thinking that make it hard to get through the day are not a normal part of aging.</li>
    <li>People with one or more of these 10 signs should talk to their doctor to find the cause. It is not always dementia.</li>
    <li>Early dementia diagnosis gives you a chance to get care and plan your future.</li>
  </ul>

  <h1 class="title">
    <span class="title-line title-line--top"><span class="t-ten">10</span> <span class="t-signs">Signs <span class="t-light">of</span></span></span>
    <span class="title-line t-teal">Thinking</span>
    <span class="title-line t-teal"><span class="t-light">or</span> Memory</span>
    <span class="title-line t-teal">Changes</span>
    <span class="title-line t-might">that Might be</span>
    <span class="title-line t-dementia">Dementia</span>
  </h1>

  <p class="intro">As we get older, we may slow down a bit. This is a normal part of aging. Changes in memory or thinking that make it harder to get through the day, are not a normal part of aging. These may be early signs of dementia. Because American Indian and Alaska Native people have a high risk of dementia, it is important to know the warning signs.</p>

  <p class="learn">To learn more about the warning signs of dementia in<br>American Indian and Alaska Native people, visit:<br>www.eldermindcircle.org | www.healthyagingnow.org</p>

  <div class="partners">
    <div class="partner partner--one"><i></i><span>NORTHERN CIRCLE<br>AGING COUNCIL</span></div>
    <div class="partner partner--two"><i></i><span>ELDER BRAIN HEALTH<br>RESOURCE HUB</span></div>
  </div>
  <div class="strip"></div>
</article>

<article class="page page--back">
  <svg class="page-art" viewBox="0 0 296 418" width="296" height="418">
    <defs>
      <linearGradient id="friends-photo" x1="0" y1="0" x2="1" y2="1">
        <stop offset="0" stop-color="#d9b2a4"/>
        <stop offset=".6" stop-color="#c98a7e"/>
        <stop offset="1" stop-color="var(--clay)"/>
      </linearGradient>
    </defs>
    <path d="M0 0H156C170 70 140 150 150 230C158 300 172 360 152 418H0Z" fill="var(--clay)"/>
    <path d="M0 0H156C166 40 158 90 150 134H0Z" fill="url(#friends-photo)" role="img" aria-label="Photo of two older friends sharing a high five at a table"/>
  </svg>

  <div class="ask">
    <p>Do you<br>have<br>any of<br>these<br>10<br>signs?</p>
    <p>If so,<br>talk to<br>your<br>doctor.</p>
  </div>

  <ol class="signs">
    <li>Memory loss that affects your daily life. You may:
      <ul><li>Forget events or important dates</li><li>Repeat yourself</li><li>Rely more often on lists or sticky notes to remember things</li></ul></li>
    <li>Trouble planning or solving problems. You may have a harder time:
      <ul><li>Paying bills</li><li>Cooking recipes you have used for years</li></ul></li>
    <li>Get confused about the time, date, or where you are.</li>
    <li>Daily tasks are getting harder, including:
      <ul><li>Driving</li><li>Making a grocery list or going shopping</li></ul></li>
    <li>Trouble with how your eyesight and thinking work together that gets worse. This includes:
      <ul><li>Tripping, falls, or problems with your balance</li><li>Spilling or dropping things more</li></ul></li>
    <li>New trouble talking or writing. You have a hard time finding the words you want to say. For example, you may say “that thing on your wrist that tells time” instead of “watch.”</li>
    <li>Lose and cannot find things. For example, you:
      <ul><li>Can’t find the coffee pot that you use every day</li><li>Might put your car keys in the freezer</li></ul></li>
    <li>Notice changes in mood or personality, such as being:
      <ul><li>Easily mad or sad in everyday situations</li><li>More fearful (scared) or suspicious (not trusting)</li></ul></li>
    <li>Act different and make poor choices. This may make you more likely to:
      <ul><li>Spend money you do not have or be a scam victim</li><li>Stop washing up regularly or pay less attention to how you look</li><li>Forget to take care of your pet</li></ul></li>
    <li>Pull away from friends and family because it is harder to keep up. You may not want to do things you used to enjoy, like sporting events, church, music, or sex.</li>
  </ol>
</article>

</body>
</html>
```